依頼概要
■依頼の目的/概要
弊社の経営理念を作成しましたが、社内掲示用にポスターの作成をお願いします。

■依頼詳細
ミッション・ビジョン・バリューをポスター1枚に収めてください。
HPにも掲載できればと考えています。

■重視する点
掲載内容は添付ファイルをご確認ください。

過去の提案(同業者なので)を見て応募しようと考えました。
https://www.pitchora.jp/work/detail/4731852

■弊社の紹介
東京都内で廃棄物を収集・処分する会社です。詳しくは下記Official HPをご覧ください。
https://www.miyakura-k.co.jp

HP検討挿入予定個所
https://www.miyakura-k.co.jp/company

■その他
掲載内容の文言はあまり整理されていないのでうまい具合にご調整ください。

■その他ご不明点はお気軽にお問合せください。

発注時のイメージ通りの作品だったため。

この度は、沢山のご応募ありがとうございます。
皆さんのご提案が多く、選定に迷いました。

また機会がございましたら、よろしくお願いします。

```html
<!DOCTYPE html>
<html lang="ja">
<head>
<meta charset="utf-8">
<title>MIYAKURA 経営理念</title>
<link rel="stylesheet" href="https://fonts.googleapis.com/css2?family=Cinzel:wght@500;600&family=Noto+Sans+JP:wght@500;700&display=swap">
<style>
  :root {
    --green: #6aaa32;
    --green-deep: #4f8f25;
    --green-light: #b9dc7c;
    --sky: #e6f3f6;
    --ink: #1d1d1d;
    --paper: #ffffff;
  }
  * { margin: 0; padding: 0; box-sizing: border-box; }
  html, body { width: 848px; height: 1200px; overflow: hidden; background: var(--paper); }
  .poster {
    position: relative;
    width: 848px; height: 1200px; overflow: hidden;
    background: radial-gradient(ellipse 75% 45% at 50% 0%, var(--sky) 0%, var(--paper) 70%);
    font-family: "Noto Sans JP", sans-serif;
    color: var(--ink);
  }
  .brand {
    position: absolute; left: 32px; top: 34px;
    display: flex; align-items: center; gap: 10px;
    font-family: "Noto Sans JP", sans-serif; font-weight: 700;
    font-size: 18px; letter-spacing: 0.08em; color: var(--green-deep);
  }
  .brand-dot { width: 22px; height: 22px; border-radius: 50%; background: var(--green); }
  .section { position: absolute; left: 0; width: 100%; text-align: center; }
  .section-mission { top: 100px; }
  .section-vision { top: 312px; }
  .section-value { top: 548px; }
  .heading {
    position: relative; display: inline-block;
    font-family: "Cinzel", serif; font-weight: 600;
    color: var(--green); font-size: 58px; letter-spacing: 0.02em; line-height: 1;
  }
  .heading .initial { font-size: 84px; }
  .heading-sub {
    position: absolute; right: 8px; top: -4px;
    font-family: "Noto Sans JP", sans-serif; font-weight: 700;
    font-size: 15px; letter-spacing: 0.06em; color: var(--green-deep);
  }
  .statement { margin-top: 22px; font-size: 17px; font-weight: 500; line-height: 28px; letter-spacing: 0.03em; }
  .scenery { position: absolute; left: 0; top: 720px; width: 848px; height: 400px; }
  .footer-band {
    position: absolute; left: 0; bottom: 0; width: 100%; height: 82px;
    background: var(--green);
    display: flex; align-items: center; justify-content: center;
  }
  .footer-name {
    font-family: "Noto Sans JP", sans-serif; font-weight: 700;
    font-size: 26px; letter-spacing: 0.1em; color: var(--paper);
  }
</style>
</head>
<body>
<main class="poster">
  <div class="brand"><span class="brand-dot"></span>MIYAKURA</div>

  <section class="section section-mission">
    <h2 class="heading"><span class="heading-sub">社会的使命</span><span class="initial">M</span>ISSION</h2>
    <p class="statement">地球環境を保全するために<br>静脈産業を支える社会インフラの一部としての役割を全うし<br>すべての人に快適でクリーンな世界を提供する</p>
  </section>

  <section class="section section-vision">
    <h2 class="heading"><span class="heading-sub">中長期計画</span><span class="initial">V</span>ISION</h2>
    <p class="statement">先進的 (Advanced) な取り組みを行い<br>廃棄物業界をリード (Lead) し、高品質 (High quality) なサービスを提供し<br>働きがいのある (Satisfaction) 会社づくりを行う</p>
  </section>

  <section class="section section-value">
    <h2 class="heading"><span class="heading-sub">大切な価値観</span><span class="initial">V</span>ALUE</h2>
    <p class="statement">活発なコミュニケーションの元、情報共有を行い<br>チームワーク溢れる組織風土の中で、共働し、何事にも真摯に向き合い<br>正直な気持ちで、チャレンジ行動力をもって、自己実現を目指す</p>
  </section>

  <svg class="scenery" viewBox="0 0 848 400" role="img" aria-label="緑のシルエットで描かれた街並み、木々、人々と車の風景イラスト">
    <defs>
      <linearGradient id="sceneryFill" x1="0" y1="0" x2="0" y2="1">
        <stop offset="0" stop-color="#d8ecb8" stop-opacity="0"/>
        <stop offset="0.45" stop-color="#b9dc7c" stop-opacity="0.7"/>
        <stop offset="1" stop-color="#7fbb3e"/>
      </linearGradient>
    </defs>
    <rect x="0" y="0" width="848" height="400" fill="url(#sceneryFill)"/>
  </svg>

  <footer class="footer-band"><span class="footer-name">MIYAKURA</span></footer>
</main>
</body>
</html>
```